Landing page for Cloud Kitchen buisnies

We need a landing page design fully functional for our Cloud Kitchen company wich is based in Dubai we have a industrial kitchen setup up from where we operate our own online food brands wich are only availble for delivery

Target Market(s)

Its just a company Profile

Requirements
Must have
• Company name is Ember Plate Holdings. We have the Logo already

LOGO AND DOMAIN WE HAVE
Nice to have
• Proffesionel high quality design

```html
<!DOCTYPE html>
<html lang="en">
<head>
<meta charset="utf-8">
<title>Ember Plate Holdings</title>
<link rel="stylesheet" href="https://fonts.googleapis.com/css2?family=Poppins:wght@500;600&display=swap">
<style>
  :root {
    --gold-dark: #a87b25;
    --gold: #c49a3a;
    --gold-light: #ead663;
    --ink: #111111;
    --board: #1c1e20;
    --board-edge: #0c0d0e;
    --white: #ffffff;
  }
  * { margin: 0; padding: 0; box-sizing: border-box; }
  html, body { width: 1200px; height: 998px; overflow: hidden; }
  body { font-family: "Poppins", sans-serif; color: var(--ink); }
  .page { position: relative; width: 1200px; height: 998px; overflow: hidden; }

  .hero-photo {
    position: absolute; inset: 0;
    background:
      radial-gradient(ellipse at 50% 45%, #2a2d30 0%, var(--board) 45%, var(--board-edge) 100%),
      var(--board);
  }
  .hero-photo .produce-left {
    position: absolute; left: 0; top: 0; width: 240px; height: 720px;
    background: linear-gradient(180deg, #3a3430 0%, #4a3f35 40%, #8b2a1c 75%, #a8321f 100%);
    opacity: .55; border-radius: 0 120px 120px 0;
  }
  .hero-photo .produce-right {
    position: absolute; right: 0; top: 0; width: 280px; height: 720px;
    background: linear-gradient(180deg, #5a1d14 0%, #3a2a24 35%, #4a3028 65%, #8a3a44 100%);
    opacity: .5; border-radius: 140px 0 0 140px;
  }

  .menu-toggle { position: absolute; left: 126px; top: 130px; width: 36px; height: 25px; display: flex; flex-direction: column; justify-content: space-between; }
  .menu-toggle span { display: block; height: 3px; background: var(--white); border-radius: 2px; }

  .brand {
    position: absolute; left: 0; right: 0; top: 160px; text-align: center;
    font-weight: 600; font-size: 30px; letter-spacing: 1px; color: var(--gold);
  }
  .brand-mark { display: block; width: 90px; height: 90px; margin: -110px auto 20px; border: 3px solid var(--gold); border-radius: 50%; }

  .auth { position: absolute; top: 97px; left: 823px; display: flex; gap: 16px; }
  .btn {
    display: inline-flex; align-items: center; justify-content: center;
    background: linear-gradient(90deg, var(--gold-dark), var(--gold-light) 60%, var(--gold));
    color: var(--white); font-weight: 600; text-decoration: none; border-radius: 40px;
  }
  .btn-small { width: 127px; height: 45px; font-size: 16px; }

  .social { position: absolute; left: 38px; top: 332px; display: flex; flex-direction: column; gap: 22px; }
  .social span { width: 16px; height: 16px; border-radius: 50%; background: var(--white); }

  .welcome { position: absolute; left: 0; right: 0; top: 326px; text-align: center; font-weight: 600; line-height: 48px; font-size: 44px; }
  .welcome .lead { color: var(--white); display: block; }
  .welcome .name { color: var(--gold); display: block; }
  .btn-order { position: absolute; left: 482px; top: 446px; width: 236px; height: 54px; font-size: 23px; }

  .wave { position: absolute; left: 0; top: 0; }

  .contact { position: absolute; left: 0; right: 0; top: 790px; }
  .contact h2 { text-align: center; font-size: 30px; font-weight: 600; line-height: 40px; }
  .contact-item { position: absolute; top: 66px; display: flex; align-items: center; gap: 14px; font-size: 15px; font-weight: 500; line-height: 18px; }
  .contact-item svg { flex: none; }
  .item-address { left: 253px; }
  .item-phone { left: 538px; }
  .item-email { left: 748px; }
  .divider { position: absolute; left: 204px; width: 793px; top: 930px; height: 1px; background: #3a3320; }
  .legal { position: absolute; left: 0; right: 0; top: 948px; text-align: center; font-size: 16px; font-weight: 500; }
</style>
</head>
<body>
<div class="page">
  <div class="hero-photo" role="img" aria-label="Dark wooden kitchen table with tomatoes, herbs, spices, garlic, oil bottle, cutting boards and a checked cloth">
    <div class="produce-left"></div>
    <div class="produce-right"></div>
  </div>

  <svg class="wave" width="1200" height="998" viewBox="0 0 1200 998" aria-hidden="true">
    <defs>
      <linearGradient id="goldBand" x1="0" x2="1" y1="0" y2="0">
        <stop offset="0" stop-color="#b58a2e"/>
        <stop offset=".3" stop-color="#e3cb5a"/>
        <stop offset=".6" stop-color="#ead663"/>
        <stop offset="1" stop-color="#b8892c"/>
      </linearGradient>
    </defs>
    <path fill="url(#goldBand)" d="M0,675 C40,700 100,718 150,715 C200,712 225,692 240,680 C300,730 380,760 450,757 C530,754 600,720 635,678 C680,720 740,740 800,737 C870,734 930,700 958,680 C1020,720 1080,730 1110,727 C1150,723 1180,708 1200,695 L1200,998 L0,998 Z"/>
  </svg>

  <div class="menu-toggle" aria-label="Menu"><span></span><span></span><span></span></div>

  <div class="brand"><span class="brand-mark"></span>Ember Plate Holdings</div>

  <nav class="auth">
    <a class="btn btn-small" href="#">SIGN UP</a>
    <a class="btn btn-small" href="#">LOGIN</a>
  </nav>

  <div class="social" aria-label="Social links"><span></span><span></span><span></span></div>

  <h1 class="welcome"><span class="lead">WELCOME TO</span><span class="name">EMBER PLATE HOLDINGS</span></h1>
  <a class="btn btn-order" href="#">ORDER FOOD</a>

  <section class="contact">
    <h2>CONTACT</h2>
    <div class="contact-item item-address">
      <svg width="36" height="36" viewBox="0 0 36 36"><circle cx="18" cy="18" r="16.5" fill="none" stroke="#111" stroke-width="2"/><path d="M18 11a4.5 4.5 0 0 0-4.5 4.5c0 3.4 4.5 8.5 4.5 8.5s4.5-5.1 4.5-8.5A4.5 4.5 0 0 0 18 11z" fill="none" stroke="#111" stroke-width="1.8"/><circle cx="18" cy="15.5" r="1.5" fill="#111"/></svg>
      <p>Sed ut peatisunde omnis<br>iste atus error sitvo</p>
    </div>
    <div class="contact-item item-phone">
      <svg width="36" height="36" viewBox="0 0 36 36"><circle cx="18" cy="18" r="16.5" fill="none" stroke="#111" stroke-width="2"/><path d="M13.5 11.5l2.6-.4 1.4 3.3-1.6 1.2c.8 1.8 2.1 3.1 3.9 3.9l1.2-1.6 3.3 1.4-.4 2.6c-.2.8-1 1.3-1.8 1.2-5-.6-8.8-4.4-9.4-9.4-.1-.8.4-1.6 1.2-1.8z" fill="#111"/></svg>
      <p>Phone:<br>555 014 2290</p>
    </div>
    <div class="contact-item item-email">
      <svg width="36" height="36" viewBox="0 0 36 36"><circle cx="18" cy="18" r="16.5" fill="none" stroke="#111" stroke-width="2"/><rect x="11" y="13" width="14" height="10" rx="1" fill="#111"/><path d="M11.5 13.5l6.5 5 6.5-5" fill="none" stroke="#e3cb5a" stroke-width="1.3"/></svg>
      <p>Email:<br>hello@emberplate.example</p>
    </div>
  </section>

  <div class="divider"></div>
  <p class="legal">© 2020 All Rights are reserved. Privacy &nbsp;|&nbsp; Terms of use</p>
</div>
</body>
</html>
```